Redesign of Business Cards to Update them!

We want a full overhaul of our business cards! We have a design that is almost 5 years old and it needs to be updated to be current

Address is 457 Calloway Court Suite B San Bernardino CA 92408
PH: 9094417382
Tindlebox.com

Hours M-F 10AM-4PM
Sat and Sunday Closed

```html
<!DOCTYPE html>
<html lang="en">
<head>
<meta charset="utf-8">
<title>Tindlebox Business Card</title>
<link rel="stylesheet" href="https://fonts.googleapis.com/css2?family=Montserrat:wght@400;600;800&display=swap">
<style>
  :root {
    --red: #f40000;
    --black: #0b0b0b;
    --white: #ffffff;
    --backdrop: #2b2b2b;
  }
  html, body {
    margin: 0;
    padding: 0;
    width: 1200px;
    height: 881px;
    overflow: hidden;
    background: var(--backdrop);
    font-family: "Montserrat", sans-serif;
  }
  .stage {
    position: relative;
    width: 1200px;
    height: 881px;
  }
  .card {
    position: absolute;
    width: 560px;
    height: 320px;
    border-radius: 22px;
    overflow: hidden;
  }
  .card--front {
    left: 320px;
    top: 90px;
    background: var(--red);
  }
  .card--back {
    left: 320px;
    top: 470px;
    background: var(--white);
  }
  .brand {
    position: absolute;
    display: flex;
    align-items: center;
    gap: 14px;
    font-weight: 800;
    color: var(--black);
    letter-spacing: 0.5px;
  }
  .card--front .brand {
    left: 0;
    right: 0;
    top: 0;
    bottom: 0;
    justify-content: center;
    font-size: 54px;
  }
  .card--back .brand {
    right: 40px;
    top: 60px;
    font-size: 46px;
  }
  .brand__dot {
    width: 34px;
    height: 34px;
    border-radius: 50%;
  }
  .card--front .brand__dot { background: var(--white); }
  .card--back .brand__dot { background: var(--red); }
  .contact-band {
    position: absolute;
    left: 0;
    top: 236px;
    width: 300px;
    height: 60px;
    background: var(--black);
    color: var(--white);
    font-size: 16px;
    line-height: 24px;
    padding: 6px 0 0 34px;
    box-sizing: border-box;
  }
  .contact-band__label {
    color: var(--red);
    font-weight: 800;
    display: inline-block;
    width: 18px;
  }
  .hours-band {
    position: absolute;
    left: 312px;
    right: 0;
    top: 196px;
    height: 100px;
    background: var(--red);
    color: var(--white);
    font-size: 16px;
    font-weight: 600;
    line-height: 26px;
    padding: 24px 0 0 22px;
    box-sizing: border-box;
    text-transform: uppercase;
  }
</style>
</head>
<body>
<main class="stage">
  <section class="card card--front" aria-label="Card front">
    <div class="brand"><span class="brand__dot"></span><span class="brand__name">Tindlebox</span></div>
  </section>

  <section class="card card--back" aria-label="Card back">
    <div class="brand"><span class="brand__dot"></span><span class="brand__name">Tindlebox</span></div>
    <div class="contact-band">
      <div><span class="contact-band__label">P</span>: 9094417382</div>
      <div><span class="contact-band__label">W</span>: www.tindlebox.com</div>
    </div>
    <div class="hours-band">
      <div>Hours M-F 10AM-4PM</div>
      <div>Sat and Sunday Closed</div>
    </div>
  </section>
</main>
</body>
</html>
```